Business Cards for Demolition & Salvage Company

We are Licensed Demolition Contractors and this business card design is for our Salvage Yard. We recycle over 95% of the building materials removed from each demolition site in which we take to our Salvage Yard for resale eg. bricks, windows, doors, kitchens, stoves, lights, fencing etc so pretty much everything.
Updates

I forgot to note that single sided business card only please.

Reason: I would like to ask if designers could please submit or re-submit their designs edited to a single sided card only. The card also does not need space for an employee name or position as our general business contact details will suffice for this project. Primary colour must be ROYAL BLUE with no exceptions please. Much appreciated and thank you to all whom have submitted designs to date and I look forward to receiving your edited designs..

Industry/Entity Type

Building

Contact Information for Business Card

Tavelund Demolition & Salvage (WA) Pty Ltd
2413 Coralbrook Parkway
UPPER SWAN WA 6069
P: (08) 9371 5068
F: (08) 9371 7725
E: salvage@tvwreck.com.au
W: tavelunddemolition.com.au

Requirements
Must have
• We have a logo that has been with our Company since 1974 so he must be included in the design - file attached. As for colours, we have always used royal blue and again this must be the primary colour used in the design. Please keep the design simple.
Nice to have
• Card can include opening hours as follows:
Opening Hours:
Monday to Friday 8am - 5.00pm
Saturday 8am - 3pm
Closed Sunday's and public holidays

```html
<!DOCTYPE html>
<html lang="en">
<head>
<meta charset="utf-8">
<title>Tavelund Demolition &amp; Salvage – Business Card</title>
<link rel="stylesheet" href="https://fonts.googleapis.com/css2?family=Arimo:wght@400;700&display=swap">
<style>
  :root {
    --stage: #e9e9ec;
    --card: #ffffff;
    --navy: #141a5c;
    --royal: #2d5fc6;
    --ink: #1b2270;
    --band-text: #ffffff;
    --mascot-blue: #3a6fd0;
    --mascot-skin: #e9b9c4;
  }
  * { box-sizing: border-box; margin: 0; padding: 0; }
  html, body {
    width: 1200px; height: 900px; overflow: hidden;
    background: var(--stage);
    font-family: "Arimo", Arial, sans-serif;
  }
  .canvas {
    position: relative; width: 1200px; height: 900px;
    display: flex; align-items: center; justify-content: center;
  }
  .business-card {
    position: relative; width: 1000px; height: 606px;
    background: var(--card);
    box-shadow: 0 10px 30px rgba(0,0,0,.18);
    overflow: hidden;
  }
  .wave { position: absolute; inset: 0; width: 100%; height: 100%; }
  .company-name {
    position: absolute; left: 52px; top: 78px;
    font-size: 34px; font-weight: 400; color: var(--ink);
    letter-spacing: .3px; white-space: nowrap;
  }
  .contact-list {
    position: absolute; right: 40px; top: 128px;
    list-style: none; text-align: right;
    color: var(--ink); font-size: 23px; line-height: 35px;
  }
  .contact-list li { display: flex; justify-content: flex-end; align-items: center; gap: 12px; }
  .contact-icon { width: 20px; height: 20px; fill: var(--ink); flex: none; }
  .mascot {
    position: absolute; left: 110px; top: 170px;
    width: 250px; height: 260px; border-radius: 36px;
    background: radial-gradient(circle at 45% 45%, var(--mascot-blue) 0%, #5c82d4 45%, var(--mascot-skin) 100%);
    opacity: .9;
  }
  .address {
    position: absolute; right: 60px; bottom: 60px;
    color: var(--band-text); font-size: 25px; white-space: nowrap;
  }
</style>
</head>
<body>
<main class="canvas">
  <article class="business-card">
    <svg class="wave" viewBox="0 0 1000 606" preserveAspectRatio="none" aria-hidden="true">
      <path fill="var(--royal)" d="M0 480 C350 480 650 370 1000 280 L1000 606 L0 606 Z"/>
      <path fill="#ffffff" d="M0 490 C350 490 650 382 1000 296 L1000 606 L0 606 Z"/>
      <path fill="var(--navy)" d="M0 498 C350 498 650 392 1000 306 L1000 606 L0 606 Z"/>
    </svg>

    <h1 class="company-name">Tavelund Demolition &amp; Salvage (WA) Pty Ltd</h1>

    <ul class="contact-list">
      <li>(08) 9371 5068
        <svg class="contact-icon" viewBox="0 0 24 24"><path d="M6.6 10.8a15 15 0 0 0 6.6 6.6l2.2-2.2c.3-.3.7-.4 1-.2 1.1.4 2.3.6 3.6.6.6 0 1 .4 1 1V20c0 .6-.4 1-1 1A17 17 0 0 1 3 4c0-.6.4-1 1-1h3.5c.6 0 1 .4 1 1 0 1.3.2 2.5.6 3.6.1.3 0 .7-.2 1z"/></svg>
      </li>
      <li>(08) 9371 7725
        <svg class="contact-icon" viewBox="0 0 24 24"><path d="M6 2h10l2 2v5H6zM3 10h18a1 1 0 0 1 1 1v7h-4v4H6v-4H2v-7a1 1 0 0 1 1-1zm5 7v3h8v-3z"/></svg>
      </li>
      <li>salvage@tvwreck.com.au
        <svg class="contact-icon" viewBox="0 0 24 24"><path d="M2 5h20v14H2zm2 2v.5l8 5 8-5V7l-8 5z"/></svg>
      </li>
      <li>tavelunddemolition.com.au
        <svg class="contact-icon" viewBox="0 0 24 24"><path d="M14 2a8 8 0 1 1-5.3 14L3.4 21.3 2 19.9l5.3-5.3A8 8 0 0 1 14 2zm0 3a5 5 0 1 0 0 10 5 5 0 0 0 0-10z"/></svg>
      </li>
    </ul>

    <div class="mascot" role="img" aria-label="Company mascot: cartoon demolition worker in hard hat swinging a sledgehammer"></div>

    <p class="address">2413 Coralbrook Parkway UPPER SWAN WA 6069</p>
  </article>
</main>
</body>
</html>
```